Letterhead for small civil engineer company

We need bold and modern design for company letterhead in MS word. It needs to have company logo and company info. Somewhere in the upper right part of document needs to be space for "recever" and the documents starts with, example, "SUBJECT: CIVIL ENGINEER LETTERHEAD".

in the bottom part of document needs to be signature and date.

Company info: Veltrana d.o.o., Lipovac 15, Lipovac (Općina Brdarić), OIB 47396028154, www.veltrana.hr, info@veltrana.hr

Email of document sender needs to be somewhere if document, exapmle xyz@veltrana.hr

Target Market(s)

Civil engineer company and projects

Industry/Entity Type

Civil engineer

Font styles to use
Serif

Colors
F0912C
F2A743
F7CA91
FBE8D2
FDF5EE

Requirements
Must have
• Company logo and company info
Nice to have
• Moder and clean design
Should not have
• Too much details

```html
<!DOCTYPE html>
<html lang="en">
<head>
<meta charset="utf-8">
<title>Veltrana Letterhead</title>
<link href="https://fonts.googleapis.com/css2?family=Lato:wght@400;700&family=Jost:wght@400&family=Great+Vibes&display=swap" rel="stylesheet">
<style>
  :root {
    --orange: #e0872d;
    --grey-dark: #6b6663;
    --grey-line: #5f5f5f;
    --ink: #3a3a3a;
    --backdrop: #e2e2e2;
    --paper: #f2f2f2;
  }
  html, body {
    margin: 0;
    padding: 0;
    width: 1153px;
    height: 1200px;
    overflow: hidden;
    background: var(--backdrop);
  }
  .letterhead {
    position: absolute;
    left: 147px;
    top: 0;
    width: 858px;
    height: 1200px;
    background: radial-gradient(circle at 62% 32%, #ffffff 0%, #fafafa 35%, var(--paper) 75%);
    font-family: "Lato", sans-serif;
    color: var(--ink);
    overflow: hidden;
  }
  .brand-mark {
    position: absolute;
    left: 137px;
    top: 47px;
    width: 74px;
    height: 74px;
    border: 2px solid var(--grey-line);
  }
  .brand-name {
    position: absolute;
    left: 66px;
    top: 131px;
    width: 222px;
    text-align: center;
    font-family: "Lato", sans-serif;
    font-weight: 400;
    font-size: 30px;
    letter-spacing: 1px;
    line-height: 1;
    color: var(--orange);
  }
  .receiver-block {
    position: absolute;
    right: 69px;
    top: 104px;
    text-align: right;
    font-size: 17.5px;
    line-height: 21px;
  }
  .receiver-block .receiver { font-weight: 700; }
  .header-rule {
    position: absolute;
    left: 63px;
    top: 193px;
    width: 728px;
    height: 3px;
    background: linear-gradient(to right, var(--grey-line) 0 57%, var(--orange) 57% 100%);
  }
  .letter-body {
    position: absolute;
    left: 66px;
    top: 292px;
    width: 725px;
  }
  .address-block {
    margin: 0;
    font-size: 16px;
    line-height: 19.7px;
  }
  .address-block + .address-block { margin-top: 19px; }
  .salutation {
    margin: 24px 0 21px;
    font-size: 19px;
    font-weight: 700;
  }
  .paragraph {
    margin: 0 0 18px;
    font-size: 15.7px;
    line-height: 18.3px;
    text-align: justify;
  }
  .closing {
    margin: 40px 0 0;
    font-size: 16px;
  }
  .signature {
    margin: 16px 0 0 2px;
    font-family: "Great Vibes", cursive;
    font-size: 42px;
    line-height: 42px;
    color: #2b2b2b;
  }
  .sign-date {
    margin: 0;
    font-size: 16.5px;
    line-height: 18px;
  }
  .footer-info {
    position: absolute;
    left: 0;
    width: 858px;
    top: 1070px;
    text-align: center;
    font-family: "Jost", sans-serif;
    font-size: 13px;
    line-height: 18.5px;
    color: #1e1e1e;
  }
  .footer-rule {
    position: absolute;
    left: 0;
    top: 1120px;
    width: 858px;
    height: 6px;
    background: var(--grey-dark);
  }
  .footer-band {
    position: absolute;
    left: 0;
    top: 1134px;
    width: 858px;
    height: 66px;
    background: var(--orange);
  }
</style>
</head>
<body>
  <main class="letterhead">
    <div class="brand-mark"></div>
    <div class="brand-name">VELTRANA</div>

    <div class="receiver-block">
      <div class="receiver">RECEVER</div>
      <div class="subject">SUBJECT: CIVIL ENGINEER LETTERHEAD</div>
    </div>

    <div class="header-rule"></div>

    <section class="letter-body">
      <p class="address-block">Feb-03-2022<br>Mr, Ivan Marić<br>President</p>
      <p class="address-block">Brook Corporation<br>123 Street Name, Suite# 10<br>City, State, 120023</p>
      <p class="salutation">Dear Mr, Ivan</p>
      <p class="paragraph">Lorem ipsum dolor sit amet, consectetur adipisicing elit, sed do eiusmod tempor incididunt ut labore et dolore magna aliqua. Ut enim ad minim veniam, quis nostrud exercitation ullamco laboris nisi ut aliquip ex ea commodo consequat. Duis aute irure dolor in reprehenderit in voluptate velit esse cillum dolore eu fugiat nulla pariatur.</p>
      <p class="paragraph">Lorem ipsum dolor sit amet, consectetur adipisicing elit, sed do eiusmod tempor incididunt ut labore et dolore magna aliqua. Ut enim ad minim veniam, quis nostrud exercitation ullamco laboris nisi ut aliquip ex ea commodo consequat. Duis aute irure dolor in reprehenderit in voluptate velit esse cillum dolore eu fugiat nulla pariatur.</p>
      <p class="paragraph">Lorem ipsum dolor sit amet, consectetur adipisicing elit, sed do eiusmod tempor incididunt ut labore et dolore magna aliqua. Ut enim ad minim veniam, quis nostrud exercitation ullamco laboris nisi ut aliquip ex ea commodo consequat.</p>
      <p class="paragraph">Excepteur sint occaecat cupidatat non proident, sunt in culpa qui officia deserunt mollit anim id est laborum. re et dolore magnam aliquam quaerat voluptatem.</p>
      <p class="closing">Regards</p>
      <p class="signature">Daniel Horvat</p>
      <p class="sign-date">Dec-12-2024</p>
    </section>

    <div class="footer-info">
      Veltrana d.o.o., Lipovac 15, Lipovac (Općina Brdarić),<br>
      OIB 47396028154, www.veltrana.hr, info@veltrana.hr
    </div>
    <div class="footer-rule"></div>
    <div class="footer-band"></div>
  </main>
</body>
</html>
```